Website for Wedding Cake Business based in Suffolk countryside

I need a website to advertise my services. I bake wedding cakes and celebration cakes. My style of baking is very rustic and I use lots of local and homegrown ingredients within my baking. I’d like the website to be classy but countryside chic. I want to website to reflect quality and sophistication but also keep the countryside vibe. My logo is currently a mustard yellow and grey but this may be changed so the colour palette is completely open.

Target Market(s)

Couples and women aged 21-40

Industry/Entity Type

Wedding

Number of Pages Required

4 page

Colors

Designer to choose colors to be used in the design.

Requirements
Must have
• Must appeal to men and women. Must have a contact button, social media links, price list and photo gallery.
• Functioning drop downs (price list, gallery, booking form)
Nice to have
• Very simple layout with menu bar across the top of the page. A section can update which shows which feeding Faye or show I’ll be a next with a map.
Should not have
• Nothing to bold, block coloured or cheesy.

```html
<!DOCTYPE html>
<html lang="en">
<head>
<meta charset="utf-8">
<title>Hazelbrook Cake House</title>
<link href="https://fonts.googleapis.com/css2?family=Merienda:wght@400;700;900&family=Lora:ital,wght@1,400;1,600&display=swap" rel="stylesheet">
<style>
:root{
  --rust:#b35a22;
  --rust-dark:#9a4a18;
  --ink:#111111;
  --paper:#ffffff;
  --muted:#555555;
  --field:#e9e9e9;
  --hero-dark:#1c1917;
  --hero-warm:#3b2a20;
}
*{box-sizing:border-box;margin:0;padding:0}
html,body{width:1200px;height:3429px;overflow:hidden;background:var(--paper)}
body{position:relative;font-family:"Lora",Georgia,serif;color:var(--ink)}
.abs{position:absolute}
.wave{position:absolute;left:0;width:1200px;height:16px;display:block}
.heading{font-family:"Merienda",cursive;font-weight:700}

/* hero */
.hero{left:0;top:0;width:1200px;height:789px;background:radial-gradient(ellipse at 70% 55%,#5a3b28 0%,var(--hero-warm) 25%,var(--hero-dark) 60%,#0e0d0c 100%)}
.topbar{left:0;top:0;width:1200px;height:100px;background:var(--rust)}
.nav{top:52px;font-family:"Merienda",cursive;font-weight:700;font-size:17px;color:var(--paper);text-transform:uppercase;display:flex;gap:42px}
.nav.left{left:150px}
.nav.right{left:732px}
.brand{left:480px;top:27px;width:224px;height:190px;background:var(--paper);border:3px solid var(--rust);display:flex;align-items:center;justify-content:center;gap:10px}
.brand-mark{width:16px;height:16px;background:var(--rust)}
.brand-name{font-family:"Merienda",cursive;font-weight:700;font-size:22px;color:var(--rust)}
.hero-title{left:112px;top:335px;font-size:52px;font-weight:900;color:var(--paper);letter-spacing:1px}
.hero-text{left:112px;top:415px;width:620px;font-size:16px;font-weight:600;line-height:31px;color:var(--paper)}
.btn-quick{left:112px;top:523px;width:226px;height:60px;background:var(--rust);color:var(--paper);font-family:"Merienda",cursive;font-weight:700;font-size:19px;display:flex;align-items:center;justify-content:center;text-transform:uppercase}
.dot{position:absolute;left:1131px;width:14px;height:14px;border-radius:50%;background:var(--paper)}
.dot.active{left:1124px;width:28px;height:28px;background:none;border:3px solid var(--paper)}
.dot.active::after{content:"";position:absolute;left:5px;top:5px;width:12px;height:12px;border-radius:50%;background:var(--paper)}

/* section titles */
.section-title{left:0;width:1200px;display:flex;justify-content:center;align-items:center;gap:18px;font-size:44px;color:var(--ink)}
.swirl{width:48px;height:20px}

/* about */
.about-sub{left:0;width:1200px;top:955px;text-align:center;font-size:46px;color:var(--rust)}
.about-text{left:263px;top:1036px;width:674px;text-align:center;font-size:14px;line-height:29px;color:var(--muted)}
.value{top:1175px;font-size:30px;color:var(--ink)}

/* gallery */
.gallery{left:0;top:1333px;width:1200px;height:605px;background:var(--rust)}
.gallery-title{left:112px;top:1418px;font-size:40px;color:var(--paper)}
.gallery-sub{left:112px;top:1482px;font-size:17px;font-weight:600;color:var(--paper)}
.btn-all{left:930px;top:1445px;width:156px;height:43px;background:var(--paper);color:var(--rust);font-family:"Merienda",cursive;font-weight:700;font-size:14px;display:flex;align-items:center;justify-content:center}
.photo{top:1545px;width:224px;height:309px;border:4px solid var(--paper)}

/* price list */
.price-row{width:464px;height:87px;border-bottom:2px dotted #9a9a9a}
.price-name{position:absolute;left:0;top:0;font-family:"Merienda",cursive;font-size:22px;color:var(--ink)}
.price-desc{position:absolute;left:0;top:32px;font-size:14px;color:var(--muted)}
.price-amt{position:absolute;right:0;top:16px;font-family:"Merienda",cursive;font-weight:700;font-size:28px;color:var(--rust)}

/* contact */
.footer{left:0;top:2740px;width:1200px;height:689px;background:var(--ink)}
.card{left:240px;top:2656px;width:716px;height:448px;background:var(--paper);box-shadow:0 4px 16px rgba(0,0,0,.25)}
.fold{left:240px;top:3046px;width:58px;height:58px}
.field{position:absolute;background:var(--field);border-radius:20px;font-size:12px;color:#777;padding:12px 24px}
.btn-submit{left:505px;top:3020px;width:188px;height:50px;border-radius:25px;background:var(--rust);color:var(--paper);font-family:"Merienda",cursive;font-weight:700;font-size:19px;display:flex;align-items:center;justify-content:center;text-transform:uppercase}
.info{top:3190px;display:flex;gap:18px;align-items:center;color:var(--paper)}
.info-label{font-size:11px;margin-bottom:8px}
.info-value{font-size:14px;line-height:22px}
.divider{top:3172px;width:1px;height:112px;background:#444}
.social{top:3328px;width:36px;height:36px;border:2px solid var(--paper);border-radius:50%}
.copyright{left:0;width:1200px;top:3380px;text-align:center;font-size:13px;color:var(--paper)}
</style>
</head>
<body>
<svg width="0" height="0" style="position:absolute">
  <defs>
    <path id="wave-edge" d="M0 0 H1220 V8 q-10 8 -20 0 t-20 0 t-20 0 t-20 0 t-20 0 t-20 0 t-20 0 t-20 0 t-20 0 t-20 0 t-20 0 t-20 0 t-20 0 t-20 0 t-20 0 t-20 0 t-20 0 t-20 0 t-20 0 t-20 0 t-20 0 t-20 0 t-20 0 t-20 0 t-20 0 t-20 0 t-20 0 t-20 0 t-20 0 t-20 0 t-20 0 t-20 0 t-20 0 t-20 0 t-20 0 t-20 0 t-20 0 t-20 0 t-20 0 t-20 0 t-20 0 t-20 0 t-20 0 t-20 0 t-20 0 t-20 0 t-20 0 t-20 0 t-20 0 t-20 0 t-20 0 t-20 0 t-20 0 t-20 0 t-20 0 t-20 0 t-20 0 t-20 0 t-20 0 t-20 0 Z"/>
    <path id="swirl" d="M2 12 C10 2 18 2 24 10 S38 18 46 8" fill="none" stroke="currentColor" stroke-width="2.5" stroke-linecap="round"/>
  </defs>
</svg>

<!-- hero -->
<div class="abs hero" role="img" aria-label="Photo of a chocolate cupcake with a lit sparkler on a dark background"></div>
<div class="abs topbar"></div>
<svg class="wave" style="top:99px" viewBox="0 0 1200 16" preserveAspectRatio="none"><use href="#wave-edge" fill="var(--rust)"/></svg>
<nav class="abs nav left"><span>Home</span><span>About Us</span><span>Gallery</span></nav>
<nav class="abs nav right"><span>Our Cakes</span><span>Price</span><span>Contact Us</span></nav>
<div class="abs brand"><span class="brand-mark"></span><span class="brand-name">Hazelbrook</span></div>
<h1 class="abs hero-title heading">HAZELBROOK CAKE HOUSE</h1>
<p class="abs hero-text">Nemo enim ipsam voluptatem quia voluptas sit aspernatur aut odit aut fugit, sed quia consequuntur magni dolores eos qui ratione voluptatem sequi nesciunt. Neque porro quisquam est, qui dolorem ipsum</p>
<div class="abs btn-quick">Quick Contact</div>
<span class="dot active" style="top:417px"></span>
<span class="dot" style="top:459px"></span>
<span class="dot" style="top:487px"></span>
<svg class="wave" style="top:781px" viewBox="0 0 1200 16" preserveAspectRatio="none"><g transform="translate(0 16) scale(1 -1)"><use href="#wave-edge" fill="var(--paper)"/></g></svg>

<!-- about -->
<h2 class="abs section-title heading" style="top:880px;font-weight:400"><svg class="swirl"><use href="#swirl"/></svg>About Us<svg class="swirl"><use href="#swirl"/></svg></h2>
<h3 class="abs about-sub heading">HAZELBROOK CAKE HOUSE</h3>
<p class="abs about-text">Lorem ipsum dolor sit amet, consectetur adipiscing elit. Suspendisse nisi et dolor ornare pellentesque. Nullam porttitor, odio id facilisis dapibus, mauris rhoncus elit, ultricies nulla eros at dui. In suscipit hendrerit leo sagittis aliquam. Integer tristique tempus urna, et pharetra urna volutpat at. Proin id enim euismod, ultricies magna sed, ultrices mauris.</p>
<span class="abs value heading" style="left:267px">Tradition</span>
<span class="abs value heading" style="left:457px">Quality</span>
<span class="abs value heading" style="left:619px">Creatyvity</span>
<span class="abs value heading" style="left:823px">Passion</span>

<!-- gallery -->
<svg class="wave" style="top:1318px" viewBox="0 0 1200 16" preserveAspectRatio="none"><g transform="translate(0 16) scale(1 -1)"><use href="#wave-edge" fill="var(--rust)"/></g></svg>
<section class="abs gallery"></section>
<svg class="wave" style="top:1937px" viewBox="0 0 1200 16" preserveAspectRatio="none"><use href="#wave-edge" fill="var(--rust)"/></svg>
<h2 class="abs gallery-title heading">PHOTO GALLERY</h2>
<p class="abs gallery-sub">Duis aute irure dolor in reprehenderit</p>
<div class="abs btn-all">View All Gallery</div>
<div class="abs photo" style="left:112px;background:linear-gradient(#4a3b30,#e8d8cc 45%,#c8352f 60%,#f1e6dc 75%,#6b5a4c)" role="img" aria-label="Layered sponge cake with cream and strawberries"></div>
<div class="abs photo" style="left:363px;background:linear-gradient(#5d6a5a,#d9c3a0 45%,#b99a70 70%,#7c7f88)" role="img" aria-label="Semi-naked cake topped with figs and berries"></div>
<div class="abs photo" style="left:613px;background:linear-gradient(#3a2a1e,#c7a24a 30%,#4a2c1a 55%,#2a1b12 80%,#6d8aa0)" role="img" aria-label="Chocolate drip cake with golden truffles"></div>
<div class="abs photo" style="left:864px;background:linear-gradient(#6b6a4e,#f2eee4 35%,#e9e1cc 70%,#8a8670)" role="img" aria-label="Tiered white wedding cake with sugar roses"></div>

<!-- price list -->
<h2 class="abs section-title heading" style="top:2026px">
  <svg class="swirl"><use href="#swirl"/></svg>PRICE LIST<svg class="swirl"><use href="#swirl"/></svg>
</h2>
<div class="abs" style="left:112px;top:2145px">
  <div class="price-row" style="position:relative"><span class="price-name">Double Chocolate Pie</span><span class="price-desc">Duis aute irure dolor in reprehenderit</span><span class="price-amt">$8.99</span></div>
  <div class="price-row" style="position:relative;margin-top:0"><span class="price-name" style="top:8px">Double Chocolate Pie</span><span class="price-desc" style="top:40px">Duis aute irure dolor in reprehenderit</span><span class="price-amt" style="top:24px">$8.99</span></div>
  <div class="price-row" style="position:relative"><span class="price-name" style="top:8px">Double Chocolate Pie</span><span class="price-desc" style="top:40px">Duis aute irure dolor in reprehenderit</span><span class="price-amt" style="top:24px">$8.99</span></div>
  <div class="price-row" style="position:relative"><span class="price-name" style="top:8px">Double Chocolate Pie</span><span class="price-desc" style="top:40px">Duis aute irure dolor in reprehenderit</span><span class="price-amt" style="top:24px">$8.99</span></div>
</div>
<div class="abs" style="left:622px;top:2145px">
  <div class="price-row" style="position:relative"><span class="price-name">Double Chocolate Pie</span><span class="price-desc">Duis aute irure dolor in reprehenderit</span><span class="price-amt">$8.99</span></div>
  <div class="price-row" style="position:relative"><span class="price-name" style="top:8px">Double Chocolate Pie</span><span class="price-desc" style="top:40px">Duis aute irure dolor in reprehenderit</span><span class="price-amt" style="top:24px">$8.99</span></div>
  <div class="price-row" style="position:relative"><span class="price-name" style="top:8px">Double Chocolate Pie</span><span class="price-desc" style="top:40px">Duis aute irure dolor in reprehenderit</span><span class="price-amt" style="top:24px">$8.99</span></div>
  <div class="price-row" style="position:relative"><span class="price-name" style="top:8px">Double Chocolate Pie</span><span class="price-desc" style="top:40px">Duis aute irure dolor in reprehenderit</span><span class="price-amt" style="top:24px">$8.99</span></div>
</div>

<!-- footer & contact -->
<svg class="wave" style="top:2725px" viewBox="0 0 1200 16" preserveAspectRatio="none"><g transform="translate(0 16) scale(1 -1)"><use href="#wave-edge" fill="var(--ink)"/></g></svg>
<footer class="abs footer"></footer>
<div class="abs card"></div>
<svg class="abs fold" viewBox="0 0 58 58"><path d="M0 0 L58 58 L0 58 Z" fill="var(--ink)"/><path d="M0 0 L58 58 L20 50 Z" fill="var(--rust)"/></svg>
<h2 class="abs section-title heading" style="top:2700px"><svg class="swirl"><use href="#swirl"/></svg>CONTACT US<svg class="swirl"><use href="#swirl"/></svg></h2>
<div class="field" style="left:313px;top:2825px;width:178px;height:40px">Name</div>
<div class="field" style="left:510px;top:2825px;width:178px;height:40px">Email</div>
<div class="field" style="left:706px;top:2825px;width:179px;height:40px">Phone</div>
<div class="field" style="left:313px;top:2885px;width:572px;height:105px">Message</div>
<div class="abs btn-submit">Submit</div>

<div class="abs info" style="left:145px">
  <svg width="30" height="52" viewBox="0 0 30 52" fill="none" stroke="#fff" stroke-width="2.5"><rect x="2" y="2" width="26" height="48" rx="4"/><line x1="2" y1="10" x2="28" y2="10"/><line x1="2" y1="40" x2="28" y2="40"/></svg>
  <div><div class="info-label">Call Us</div><div class="info-value">(555)-014 2290</div></div>
</div>
<div class="abs divider" style="left:354px"></div>
<div class="abs info" style="left:390px">
  <svg width="50" height="38" viewBox="0 0 50 38" fill="none" stroke="#fff" stroke-width="2.5"><rect x="2" y="2" width="46" height="34"/><path d="M2 2 L25 22 L48 2 M2 36 L19 17 M48 36 L31 17"/></svg>
  <div><div class="info-label">Email</div><div class="info-value">info@hazelbrookcakes.com</div></div>
</div>
<div class="abs divider" style="left:754px"></div>
<div class="abs info" style="left:785px">
  <svg width="40" height="52" viewBox="0 0 40 52" fill="none" stroke="#fff" stroke-width="2.5"><path d="M20 38 C10 26 8 20 8 16 A12 12 0 0 1 32 16 C32 20 30 26 20 38 Z"/><circle cx="20" cy="16" r="4"/><ellipse cx="20" cy="44" rx="17" ry="5"/></svg>
  <div><div class="info-label">Address</div><div class="info-value">#10, Duis aute irure dolor in<br>reprehenderit in voluptate</div></div>
</div>

<span class="abs social" style="left:515px" role="img" aria-label="Social link 1"></span>
<span class="abs social" style="left:558px" role="img" aria-label="Social link 2"></span>
<span class="abs social" style="left:602px" role="img" aria-label="Social link 3"></span>
<span class="abs social" style="left:645px" role="img" aria-label="Social link 4"></span>
<p class="abs copyright">© Copyrights 2019 | All Rights Reserved</p>
</body>
</html>
```